Online religious stickers company needs a letterhead design

I need a letterhead design for a startup internet company that sells religious stickers and magnets. I would like to see a design that incorporates the color blue any shade of blue is fine. Maybe the use of very light clouds signifying heaven but it is not necessary. I am attaching my logo the color can be changed if necessary.
I do not want something that is very busy. Simple is better.

Religious

```html
<!DOCTYPE html>
<html lang="en">
<head>
<meta charset="utf-8">
<title>Letterhead</title>
<link rel="stylesheet" href="https://fonts.googleapis.com/css2?family=PT+Sans+Narrow:wght@400;700&display=swap">
<style>
  :root {
    --backdrop: #e9e9ea;
    --paper: #fbfbfb;
    --brand-blue: #1b2a8f;
    --cloud-light: #eceef6;
    --cloud-mid: #c9cde3;
  }
  html, body {
    margin: 0;
    width: 1200px;
    height: 795px;
    overflow: hidden;
    background: var(--backdrop);
    font-family: "PT Sans Narrow", "Arial Narrow", sans-serif;
  }
  .letterhead {
    position: absolute;
    left: 333px;
    top: 20px;
    width: 534px;
    height: 755px;
    background: var(--paper);
    box-shadow: 0 2px 10px rgba(0,0,0,0.12);
    overflow: hidden;
  }
  .header-rule {
    position: absolute;
    left: 0;
    right: 0;
    top: 96px;
    height: 3px;
    background: var(--brand-blue);
  }
  .brand-name {
    position: absolute;
    left: 50%;
    top: 97px;
    transform: translate(-50%, -50%);
    padding: 0 14px;
    background: var(--paper);
    color: var(--brand-blue);
    font-weight: 700;
    font-size: 26px;
    letter-spacing: 1px;
    line-height: 1;
  }
  .cloud-band {
    position: absolute;
    left: 0;
    right: 0;
    bottom: 0;
    height: 300px;
    background:
      radial-gradient(ellipse 70% 55% at 100% 100%, var(--cloud-mid) 0%, var(--cloud-light) 60%, transparent 80%),
      radial-gradient(ellipse 60% 30% at 40% 100%, var(--cloud-light) 0%, transparent 75%);
  }
  .contact {
    position: absolute;
    right: 30px;
    bottom: 34px;
    text-align: right;
    color: var(--brand-blue);
    font-size: 12px;
    line-height: 1.55;
  }
  .contact .address::before {
    content: "";
    display: inline-block;
    width: 70px;
    height: 1px;
    margin-right: 6px;
    vertical-align: middle;
    background: var(--brand-blue);
  }
  .contact b { font-weight: 700; }
</style>
</head>
<body>
  <main class="letterhead">
    <div class="header-rule"></div>
    <div class="brand-name">HALO</div>
    <div class="cloud-band" role="img" aria-label="Soft pale blue clouds rising along the bottom of the page"></div>
    <footer class="contact">
      <div class="address">Suite 102 Street name, State, Zip 20345 Country</div>
      <div class="lines"><b>P:</b> 123 345 9876 <b>F:</b> 345 345 9876 <b>E:</b> info@yourname.com <b>W:</b> yourweb.com</div>
    </footer>
  </main>
</body>
</html>
```